Desing for real estate offers- Package system

The word should be graphically clear and understandable. There are 3 packages that the customer can buy: the basic package is red, the medicinal package is green and the carefree package is blue. See the Word document in the appendix. End file should be a Word, as we need to chance the text. It should also match the website as well as the business card.
https://brelvona.domistra.ch/
Colors:
Green 1: R: 187, G: 214, B: 49
Green 2: R: 119, G: 187, W: 66

Target Market(s)

Real estate company

Font styles to use
Serif
Sans Serif

```html
<!DOCTYPE html>
<html lang="de">
<head>
<meta charset="utf-8">
<title>Brelvona – Individuelle Vermarktungspakete</title>
<link href="https://fonts.googleapis.com/css2?family=Carlito:wght@400;700&family=Roboto:wght@400;700&display=swap" rel="stylesheet">
<style>
  :root {
    --green-1: #bbd631;
    --green-2: #77bb42;
    --red: #ff5050;
    --blue: #4472c4;
    --grey-text: #8a8a8a;
    --intro-text: #808080;
    --footer: #555555;
    --white: #ffffff;
  }
  * { box-sizing: border-box; margin: 0; padding: 0; }
  html, body { width: 975px; height: 1200px; overflow: hidden; background: var(--white); }
  body { position: relative; font-family: "Carlito", "Calibri", sans-serif; }

  .header { position: absolute; left: 0; top: 0; width: 975px; height: 95px; }
  .header svg { position: absolute; left: 0; top: 0; }
  .brand {
    position: absolute; left: 81px; top: 22px;
    font-size: 40px; font-weight: 700; color: var(--green-1); letter-spacing: 0.5px;
  }
  .page-title {
    position: absolute; left: 560px; top: 50px; width: 370px; text-align: center;
    font-size: 21px; font-weight: 700; color: var(--white);
  }

  .intro {
    position: absolute; left: 80px; top: 112px; width: 815px; text-align: center;
    font-size: 16.5px; line-height: 21px; color: var(--intro-text);
  }

  .package { position: absolute; top: 170px; width: 396px; height: 527px; }
  .package--basis { left: 53px; }
  .package--medium { left: 527px; }
  .package__head {
    height: 110px; border-radius: 22px 22px 0 0; text-align: center; color: var(--white);
    font-family: "Roboto", Arial, sans-serif; padding-top: 16px;
  }
  .package--basis .package__head { background: var(--red); }
  .package--medium .package__head { background: var(--blue); }
  .package__name { font-size: 17.5px; font-weight: 700; }
  .package__price { font-size: 14.5px; margin-top: 12px; }
  .package__body {
    position: absolute; left: -3px; right: -3px; top: 82px; bottom: 0;
    background: var(--white); border-radius: 18px;
    box-shadow: 0 4px 10px rgba(0,0,0,0.10);
    list-style: none; text-align: center; padding: 13px 28px 0;
  }
  .package__body li {
    font-size: 12.5px; line-height: 14px; color: var(--grey-text); margin-bottom: 13px;
  }

  .carefree {
    position: absolute; left: 0; top: 717px; width: 975px; height: 365px;
    background: var(--green-2); color: var(--white);
  }
  .carefree__title { position: absolute; left: 103px; top: 16px; font-size: 21px; font-weight: 700; }
  .carefree__price { position: absolute; left: 185px; top: 21px; font-size: 15px; font-weight: 700; }
  .carefree__list {
    position: absolute; top: 58px; list-style: none;
    font-size: 15px; font-weight: 700; line-height: 19.5px;
  }
  .carefree__list--left { left: 126px; width: 300px; }
  .carefree__list--right { left: 600px; width: 300px; }
  .carefree__list li { position: relative; }
  .carefree__list li::before {
    content: ""; position: absolute; left: -28px; top: 6px; width: 6px; height: 6px; background: var(--white);
  }

  .footer {
    position: absolute; left: 0; top: 1082px; width: 975px; height: 118px;
    background: var(--footer); color: var(--white);
    font-size: 15px; font-weight: 700; line-height: 19.5px;
  }
  .footer__col { position: absolute; top: 24px; }
  .footer__col--company { left: 51px; }
  .footer__col--office { left: 208px; }
  .footer__col--meeting { left: 464px; }
  .footer__col--contact { left: 723px; }
</style>
</head>
<body>
  <header class="header">
    <svg width="975" height="95" viewBox="0 0 975 95" aria-hidden="true">
      <polyline points="0,86 468,86 537,21 975,21" fill="none" stroke="var(--green-1)" stroke-width="9"/>
      <polygon points="493,92 551,37 975,37 975,92" fill="var(--green-2)"/>
    </svg>
    <div class="brand">Brelvona</div>
    <h1 class="page-title">Individuelle Vermarktungspakete</h1>
  </header>

  <p class="intro">Unterlagen müssen gestellt werden, ansonsten werden Sie 1:1 verrechnet: GB-Auszug,GVZ,<br>Nebenkostenabrechnung, STWEG-Protokolle der letzten 3 Jahren, …</p>

  <section class="package package--basis">
    <div class="package__head">
      <div class="package__name">Basis-Paket:</div>
      <div class="package__price">8'500.- CHF exkl. MWST</div>
    </div>
    <ul class="package__body">
      <li>Begehung Verkaufsobjekt</li>
      <li>Hedonische Schätzung intern &amp; Bank</li>
      <li>Marketing &amp; Vertriebskonzept</li>
      <li>Unterlagen einfordern- STWEG Protokolle, GB Auszug u.s.w wenn nötig</li>
      <li>Fotografieren &amp; Ausmessen der<br>Immobilie</li>
      <li>Grundriss zeichnen</li>
      <li>Dokumentation erstellen</li>
      <li>Immobilie Online aufbereiten &amp; Aufschalten</li>
      <li>Interessenten &amp; Kaufangebote prüfen</li>
      <li>Käufer zusage- andere noch vertrösten</li>
      <li>Erstellung erster Kaufvertragsentwurf</li>
    </ul>
  </section>

  <section class="package package--medium">
    <div class="package__head">
      <div class="package__name">Medium-Paket:</div>
      <div class="package__price">10'900 CHF exkl. MWST</div>
    </div>
    <ul class="package__body">
      <li>Begehung Verkaufsobjekt</li>
      <li>Hedonische Schätzung intern &amp; Bank</li>
      <li>Marketing &amp; Vertriebskonzept</li>
      <li>Unterlagen einfordern- STWEG Protokolle, GB Auszug u.s.w wenn nötig</li>
      <li>Fotografieren &amp; Ausmessen der Immobilie</li>
      <li>Grundriss zeichnen</li>
      <li>Dokumentation erstellen</li>
      <li>Unsere Interessenten anschreiben</li>
      <li>Immobilie Online aufbereiten &amp; Aufschalten</li>
      <li>Anfragen beantworten- telefonisch &amp; elektronisch</li>
      <li>Interessenten &amp; Kaufangebote prüfen</li>
      <li>Evt. Bieterverfahren modern oder altmodisch</li>
      <li>Käufer zusage- andere noch vertrösten</li>
      <li>Erstellung erster Kaufvertragsentwurf</li>
      <li>Begleitung aufs Notariat</li>
    </ul>
  </section>

  <section class="carefree">
    <h2 class="carefree__title">Sorglos:</h2>
    <div class="carefree__price">2% vom Verkaufspreis inkl. MWST (von Grundstückgewinnsteuer abziehbar)</div>
    <ul class="carefree__list carefree__list--left">
      <li>Begehung Verkaufsobjekt</li>
      <li>Hedonische Schätzung intern &amp; Bank</li>
      <li>Marketing &amp; Vertriebskonzept</li>
      <li>Unterlagen einfordern- STWEG Protokolle, GB Auszug u.s.w wenn nötig</li>
      <li>Fotografieren &amp; Ausmessen der Immobilie</li>
      <li>Grundriss zeichnen</li>
      <li>Dokumentation erstellen</li>
      <li>Unsere Interessenten anschreiben</li>
      <li>Immobilie Online aufbereiten &amp; Aufschalten</li>
      <li>Anfragen beantworten- telefonisch &amp; elektronisch</li>
      <li>Besichtigungen koordinieren</li>
    </ul>
    <ul class="carefree__list carefree__list--right">
      <li>Besichtigungen Durchführen</li>
      <li>Interessenten &amp; Kaufangebote prüfen</li>
      <li>Evt. Bieterverfahren modern oder altmodisch</li>
      <li>Käufer zusage- andere noch vertrösten</li>
      <li>Sicherheitsnachweis (SINA)- organisieren</li>
      <li>Erstellung erster Kaufvertragsentwurf</li>
      <li>Berechnung provisorische Grundstückgewinnsteuer- Steueramt</li>
      <li>Beurkundungstermin vereinbaren</li>
      <li>Begleitung aufs Notariat</li>
      <li>Eigentumsübertragung vereinbaren</li>
      <li>Helfen bei der Steuererklärung für die definitive Grundstückgewinnsteuer</li>
    </ul>
  </section>

  <footer class="footer">
    <div class="footer__col footer__col--company">Brelvona<br>8706 Meilen</div>
    <div class="footer__col footer__col--office">Externes Büro<br>Halvaro Finanz GmbH<br>Uferweg 12<br>8707 Uetikon am See</div>
    <div class="footer__col footer__col--meeting">Externes Sitzungszimmer<br>Rebhalde Forum<br>Hofweg 22<br>8702 Zollikon</div>
    <div class="footer__col footer__col--contact">T +41 44 000 12 34<br>info@brelvona.ch<br>www.brelvona.ch</div>
  </footer>
</body>
</html>
```